Logo & Graphic Design for Children's Event

We need help designing the logo and marketing materials for our summer children's event "Star Parade". This program is for children ages 5-10 and should have a bold, fun feel to it. I would like a strong logo that is the primary feature of the design with additional supporting artwork elements that can be used flexibly in a variety of formats and mediums. I would like the design to capture the overall feel of the event. This event will be themed like a TV game show/variety show and should reflect this vibe.

This design will be used for outside marketing and branding and needs to be provided in a vector format. The types of mediums it would be used on is yard signs, banners, door hangers, social media, etc. (Samples of materials from previous events included in the uploaded files to help you get a feel for the quality and tone that we aim for with this event.)

Target Market(s)

Families with children ages 5-10

Industry/Entity Type

Church

Requirements
Must have
• - Strong logo that communicates the feel of the event and includes the name "Star Parade". - Flexible supporting artwork elements that can be used in a variety of mediums. - Must use fonts that are available from free, open sources or can be provided upon delivery of completed project. - Must be kid and family friendly - Event date June 10-14 must be included - Event time 6:30-8:30pm included - Include our church logo attached - Event web address Brightpathhollow.com/KDC
Nice to have
• - A themed background that could be adapted for use on powerpoint.
Should not have
• - Any content that is scary, violent or not suitable for an audience of children.

```html
<!DOCTYPE html>
<html lang="en">
<head>
<meta charset="utf-8">
<title>Star Parade – Kids Event Poster</title>
<link href="https://fonts.googleapis.com/css2?family=Anton&family=Patrick+Hand&family=Roboto+Condensed:wght@700&display=swap" rel="stylesheet">
<style>
  :root {
    --navy: #1e1a6e;
    --navy-deep: #171458;
    --beam: #1aa3e8;
    --beam-soft: #2a6fc4;
    --neon: #6fd4ff;
    --neon-glow: #1c9cff;
    --gold: #ffe93a;
    --orange: #f47a20;
    --band: #f7941d;
    --ink: #231f20;
    --white: #ffffff;
    --streak-orange: #f15a24;
    --streak-yellow: #fbb03b;
    --streak-green: #a6d04f;
  }
  * { margin: 0; padding: 0; box-sizing: border-box; }
  html, body { width: 848px; height: 1200px; overflow: hidden; background: var(--navy); }
  .poster {
    position: relative;
    width: 848px;
    height: 1200px;
    overflow: hidden;
    background: radial-gradient(ellipse at 50% 30%, #22208a 0%, var(--navy) 55%, var(--navy-deep) 100%);
  }
  .stage-lights { position: absolute; inset: 0; }

  .event-title {
    position: absolute;
    left: 0; right: 0;
    top: 205px;
    text-align: center;
    font-family: "Anton", sans-serif;
    text-transform: uppercase;
    line-height: 0.92;
    letter-spacing: 4px;
    background: radial-gradient(ellipse at 50% 45%, var(--gold) 30%, var(--orange) 85%);
    -webkit-background-clip: text;
    background-clip: text;
    color: transparent;
  }
  .event-title .line-one { display: block; font-size: 300px; }
  .event-title .line-two { display: block; font-size: 250px; }

  .neon-frames { position: absolute; inset: 0; }
  .event-detail {
    position: absolute;
    font-family: "Patrick Hand", cursive;
    color: var(--white);
    font-size: 31px;
    letter-spacing: 1px;
    white-space: nowrap;
    transform: translate(-50%, -50%);
  }
  .audience { left: 427px; top: 891px; }
  .dates { left: 266px; top: 980px; }
  .hours { left: 518px; top: 968px; }

  .footer-band { position: absolute; inset: 0; }
  .church-mark {
    position: absolute;
    left: 124px; top: 1103px;
    display: flex; align-items: center; gap: 8px;
    font-family: "Roboto Condensed", sans-serif;
    font-weight: 700;
    color: var(--ink);
  }
  .church-mark .badge {
    width: 68px; height: 68px; border-radius: 50%;
    background: var(--ink);
  }
  .church-mark .name { line-height: 1; }
  .church-mark .name-main { display: block; font-size: 25px; }
  .church-mark .name-sub { display: block; font-size: 11px; letter-spacing: 0.5px; }
  .web-link {
    position: absolute;
    left: 354px; top: 1118px;
    display: flex; align-items: center; gap: 12px;
    font-family: "Roboto Condensed", sans-serif;
    font-weight: 700;
    font-size: 36px;
    color: var(--ink);
  }
</style>
</head>
<body>
<main class="poster">

  <svg class="stage-lights" width="848" height="1200" viewBox="0 0 848 1200" aria-hidden="true">
    <polygon points="270,0 580,0 700,820 150,820" fill="var(--beam-soft)" opacity="0.55"/>
    <polygon points="330,0 520,0 610,700 240,700" fill="var(--beam)" opacity="0.45"/>
    <polygon points="0,360 260,0 300,0 40,820 0,820" fill="var(--beam-soft)" opacity="0.35"/>
    <polygon points="848,300 600,0 640,0 848,200" fill="var(--beam-soft)" opacity="0.35"/>
    <polygon points="0,860 110,770 0,930" fill="var(--streak-yellow)"/>
    <polygon points="0,960 115,810 0,1000" fill="var(--streak-orange)"/>
    <polygon points="848,420 765,598 848,480" fill="var(--beam)"/>
    <polygon points="848,530 770,628 848,560" fill="var(--streak-green)"/>
  </svg>

  <h1 class="event-title">
    <span class="line-one">Star</span>
    <span class="line-two">Parade</span>
  </h1>

  <svg class="neon-frames" width="848" height="1200" viewBox="0 0 848 1200" aria-hidden="true">
    <defs>
      <filter id="neon-glow" x="-20%" y="-20%" width="140%" height="140%">
        <feGaussianBlur stdDeviation="4" result="blur"/>
        <feMerge><feMergeNode in="blur"/><feMergeNode in="blur"/><feMergeNode in="SourceGraphic"/></feMerge>
      </filter>
    </defs>
    <g fill="none" stroke="var(--neon)" stroke-width="3.5" stroke-linecap="round" stroke-linejoin="round" filter="url(#neon-glow)">
      <path d="M652,800 L652,836 Q652,855 630,855 L222,855 Q202,855 202,875 L202,902 Q202,922 222,922 L640,930 Q664,932 664,952 L664,985 Q664,1001 644,1001 L385,1001 Q368,1001 368,984 L368,965 Q368,950 354,950 L166,949 Q150,949 150,965 L150,982 Q150,998 166,999 L302,1008 Q316,1010 316,1024 L316,1036"/>
    </g>
  </svg>

  <p class="event-detail audience">FOR CHILDREN AGES 5-10</p>
  <p class="event-detail dates">JUNE 10-14</p>
  <p class="event-detail hours">6:30-8:30pm</p>

  <svg class="footer-band" width="848" height="1200" viewBox="0 0 848 1200" aria-hidden="true">
    <path d="M40,1200 Q90,1065 200,1065 L660,1065 Q770,1065 810,1200 Z" fill="var(--band)"/>
  </svg>

  <div class="church-mark">
    <span class="badge"></span>
    <span class="name">
      <span class="name-main">BRIGHT PATH</span>
      <span class="name-sub">COMMUNITY CHURCH</span>
    </span>
  </div>

  <div class="web-link">
    <svg width="14" height="20" viewBox="0 0 14 20" aria-hidden="true">
      <path d="M1,1 L13,12 L7,12 L10,19 L8,19.5 L5,13 L1,17 Z" fill="var(--white)"/>
    </svg>
    <span>Brightpathhollow.com/KDC</span>
  </div>

</main>
</body>
</html>
```